New Property management company business cards

Looking for a new business card, to reflect new younger ownership
Card should be clean, simple and professional but with a modern layout that is conveys our new logo and business model

Key aspects of the business:

Property Management
Facility Maintenance
Project Management
Tenant Improvements

Mailing Address:
PO BOX 7186
Ridgeford CA, 95417

Phone: 209-614-8837
Direct: 209-614-8831

Doyle Farrant
President

Target Market(s)

Commercial property owners

Industry/Entity Type

Real Estate property management

Contact Information for Business Card

Open to all designs but lean toward vertical layouts

Requirements
Must have
• Logo and space to customize name and contact info

```html
<!DOCTYPE html>
<html lang="en">
<head>
<meta charset="utf-8">
<title>Vantora Property Management – Business Card</title>
<link rel="stylesheet" href="https://fonts.googleapis.com/css2?family=Marcellus+SC&family=Montserrat:wght@400;600&display=swap">
<style>
  :root {
    --page-bg: #d9d9db;
    --teal: #3fcfc9;
    --slate: #565a6b;
    --slate-dark: #4a4d5e;
    --ink: #5b5d66;
    --white: #ffffff;
  }
  * { box-sizing: border-box; margin: 0; padding: 0; }
  html, body { width: 1200px; height: 900px; overflow: hidden; }
  body {
    background: var(--page-bg);
    display: flex;
    flex-direction: column;
    align-items: center;
    justify-content: center;
    gap: 50px;
  }
  .card {
    position: relative;
    width: 560px;
    height: 320px;
    border: 8px solid var(--teal);
    box-shadow: 0 10px 24px rgba(0,0,0,0.18);
  }

  /* Front */
  .card-front { background: var(--white); }
  .brand {
    position: absolute;
    left: 34px;
    top: 30px;
    display: flex;
    align-items: center;
    gap: 10px;
    font-family: "Montserrat", sans-serif;
    font-weight: 600;
    color: var(--slate);
  }
  .brand-mark {
    width: 16px; height: 16px;
    background: var(--teal);
  }
  .brand-name { font-size: 22px; letter-spacing: 5px; line-height: 1; }
  .brand-sub { display: block; font-size: 7px; letter-spacing: 3px; margin-top: 4px; }
  .person {
    position: absolute;
    left: 34px;
    top: 78px;
    font-family: "Montserrat", sans-serif;
  }
  .person-name { font-size: 21px; color: var(--slate); font-weight: 400; }
  .person-title { font-size: 13px; color: var(--teal); font-weight: 400; margin-top: 2px; }
  .divider {
    position: absolute;
    left: 26px; right: 26px;
    top: 152px;
    height: 1px;
    background: var(--teal);
  }
  .services {
    position: absolute;
    right: 30px;
    top: 52px;
    list-style: none;
    text-align: right;
    font-family: "Marcellus SC", serif;
    color: var(--teal);
    font-size: 15px;
    line-height: 20px;
  }
  .contact {
    font-family: "Marcellus SC", serif;
    color: var(--ink);
    font-size: 14px;
    line-height: 20px;
  }
  .contact .label { color: var(--teal); }
  .contact-phone { position: absolute; left: 34px; top: 172px; }
  .contact-mail { position: absolute; right: 30px; bottom: 26px; text-align: left; }

  /* Back */
  .card-back {
    background: var(--slate-dark);
    display: flex;
    align-items: center;
    justify-content: center;
  }
  .back-texture {
    position: absolute;
    inset: 0;
    background: linear-gradient(135deg, #5a5d6e 0%, #4c4f60 50%, #55586a 100%);
  }
  .back-brand {
    position: relative;
    display: flex;
    align-items: center;
    gap: 16px;
    font-family: "Montserrat", sans-serif;
    font-weight: 600;
    color: var(--white);
    text-align: left;
  }
  .back-brand .brand-mark { width: 26px; height: 26px; }
  .back-brand .brand-name { font-size: 44px; letter-spacing: 9px; }
  .back-brand .brand-sub { font-size: 13px; letter-spacing: 6px; margin-top: 8px; }
</style>
</head>
<body>
  <section class="card card-front">
    <div class="brand">
      <span class="brand-mark"></span>
      <div>
        <span class="brand-name">VANTORA</span>
        <span class="brand-sub">PROPERTY MANAGEMENT</span>
      </div>
    </div>
    <div class="person">
      <p class="person-name">Doyle Farrant</p>
      <p class="person-title">President</p>
    </div>
    <ul class="services">
      <li>Property Management</li>
      <li>Facility Maintenance</li>
      <li>Project Management</li>
      <li>Tenant Improvements</li>
    </ul>
    <div class="divider"></div>
    <div class="contact contact-phone">
      <p><span class="label">Phone:</span> 209-614-8837</p>
      <p>Direct: 209-614-8831</p>
    </div>
    <div class="contact contact-mail">
      <p><span class="label">Mailing Address:</span> PO BOX 7186</p>
      <p>Ridgeford CA, 95417</p>
    </div>
  </section>

  <section class="card card-back">
    <div class="back-texture" role="img" aria-label="Tonal repeating brand pattern in slate grey"></div>
    <div class="back-brand">
      <span class="brand-mark"></span>
      <div>
        <span class="brand-name">VANTORA</span>
        <span class="brand-sub">PROPERTY MANAGEMENT</span>
      </div>
    </div>
  </section>
</body>
</html>
```